Commercial Construction Company

We need a business card design based on our current logo. We are a commercial general contractor based in Southern California that specializes in bank remodels. We would like to see designs that incorporate dark blue. The final design should portray an image of professionalism and quality.

If possible, I would like to add metallic foil to the design. Thank you

```html
<!DOCTYPE html>
<html lang="en">
<head>
<meta charset="utf-8">
<title>Harlow Commercial Builders – Business Card</title>
<link href="https://fonts.googleapis.com/css2?family=Lato:wght@400;700;900&display=swap" rel="stylesheet">
<style>
  :root {
    --backdrop: #5f5f5f;
    --card: #0a0a0c;
    --card-edge: #174f8c;
    --brand-blue: #1c5aa0;
    --text-light: #e9e9ea;
    --divider: #3a3a3e;
  }
  * { margin: 0; padding: 0; box-sizing: border-box; }
  html, body {
    width: 1200px; height: 900px; overflow: hidden;
    background: var(--backdrop);
    font-family: "Lato", sans-serif;
  }
  .stage {
    width: 1200px; height: 900px;
    display: flex; align-items: center; justify-content: center; gap: 44px;
  }
  .card {
    width: 540px; height: 309px;
    background: var(--card);
    border-bottom: 3px solid var(--card-edge);
    border-right: 2px solid var(--card-edge);
    box-shadow: 0 12px 30px rgba(0,0,0,.45);
    position: relative;
    color: var(--text-light);
  }
  .brand {
    display: flex; align-items: center; gap: 12px;
    font-weight: 900; color: #ffffff;
    letter-spacing: .5px; line-height: 1.1;
  }
  .brand-dot {
    flex: none; border-radius: 50%; background: var(--brand-blue);
  }
  /* contact side */
  .card--contact .brand {
    position: absolute; left: 34px; top: 0; bottom: 0; width: 190px;
    font-size: 21px;
  }
  .card--contact .brand-dot { width: 26px; height: 26px; }
  .card--contact .divider {
    position: absolute; left: 238px; top: 58px; bottom: 58px;
    width: 1px; background: var(--divider);
  }
  .details {
    position: absolute; left: 262px; top: 62px; right: 20px;
  }
  .details .name {
    color: var(--brand-blue); font-weight: 900;
    font-size: 27px; letter-spacing: .5px; text-transform: uppercase;
  }
  .details .role { font-size: 17px; margin: 2px 0 10px; }
  .details .line { font-size: 16px; line-height: 1.32; display: flex; align-items: center; gap: 8px; }
  .details .line svg { width: 14px; height: 14px; flex: none; }
  .details .plain { padding-left: 22px; }
  /* logo side */
  .card--logo .brand {
    position: absolute; inset: 0; justify-content: center;
    font-size: 30px;
  }
  .card--logo .brand-dot { width: 36px; height: 36px; }
</style>
</head>
<body>
<main class="stage">
  <section class="card card--contact">
    <div class="brand"><span class="brand-dot"></span><span>Harlow Commercial Builders</span></div>
    <div class="divider"></div>
    <div class="details">
      <p class="name">John Smith</p>
      <p class="role">Founder &amp; CEO</p>
      <p class="line plain">1234 First Line Address</p>
      <p class="line plain">5678 Second Line Address</p>
      <p class="line">
        <svg viewBox="0 0 16 16" aria-hidden="true"><path d="M4 1.5l2.5 3-1.5 1.8c.9 1.8 2.4 3.3 4.2 4.2L11 9l3 2.5-1.5 2.5C7 14 2 9 2 3.5z" fill="var(--brand-blue)"/></svg>
        1234567890
      </p>
      <p class="line">
        <svg viewBox="0 0 16 16" aria-hidden="true"><rect x="1" y="3" width="14" height="10" fill="var(--brand-blue)"/><path d="M1 3l7 6 7-6" stroke="#0a0a0c" stroke-width="1.4" fill="none"/></svg>
        info@yourmail.com
      </p>
      <p class="line">
        <svg viewBox="0 0 16 16" aria-hidden="true"><circle cx="8" cy="8" r="6.5" fill="none" stroke="var(--brand-blue)" stroke-width="1.5"/><path d="M1.5 8h13M8 1.5c-3 3.5-3 9.5 0 13M8 1.5c3 3.5 3 9.5 0 13" stroke="var(--brand-blue)" stroke-width="1.1" fill="none"/></svg>
        www.yourwebsite.com
      </p>
    </div>
  </section>

  <section class="card card--logo">
    <div class="brand"><span class="brand-dot"></span><span>Harlow Commercial Builders</span></div>
  </section>
</main>
</body>
</html>
```